Invitation Design Project

I need a customized graphic design for my wedding invitation.I want it to be non-traditional wedding invite. The design in mind is like a movie poster graphics while adopting 'the brighter days of the islands' font style and colors that create a light mood at the front page.Inside pages can be similar to movie posters with dark background similar to that of Ashen warden.Wedding related art/graphics can be integrated within the design.Wordings can be discussed later.

Industry/Entity Type

Graphic Design

Requirements
Must have
• Other must have features are our pictures as couple which will be sent .
Nice to have
• we would like to have the words

"our wedding.

more fun if you'll come!"

on the front cover.

```html
<!DOCTYPE html>
<html lang="en">
<head>
<meta charset="utf-8">
<title>We Invite You to Our Wedding</title>
<link rel="stylesheet" href="https://fonts.googleapis.com/css2?family=Poppins:wght@600&display=swap">
<style>
  :root {
    --ink: #2e2a7a;
    --navy: #1f1c5c;
    --sky: #3d8fd8;
    --orange: #f08a2a;
    --gold: #f2b21e;
    --flame: #e8582a;
    --red: #c8232a;
    --band-orange: #ec8a3c;
    --band-blue: #3474c4;
    --band-deep: #24438e;
    --band-yellow: #f4c43a;
    --veil: rgba(255, 238, 228, 0.55);
  }
  * { margin: 0; padding: 0; box-sizing: border-box; }
  html, body { width: 856px; height: 1200px; overflow: hidden; background: #fff; }
  .invite {
    position: relative;
    width: 856px;
    height: 1200px;
    overflow: hidden;
  }
  .pattern-field {
    position: absolute;
    inset: 0;
    background: linear-gradient(180deg,
      var(--band-orange) 0%,
      #f0a070 10%,
      var(--band-blue) 24%,
      var(--band-deep) 40%,
      #6e86c8 50%,
      var(--band-orange) 60%,
      var(--band-yellow) 66%,
      var(--band-blue) 78%,
      var(--band-orange) 88%,
      var(--band-yellow) 94%,
      var(--band-orange) 100%);
  }
  .light-column {
    position: absolute;
    top: 0;
    bottom: 0;
    left: 71px;
    width: 520px;
    background: var(--veil);
  }
  .headline {
    position: absolute;
    left: 104px;
    top: 66px;
    font-family: "Poppins", sans-serif;
    font-weight: 600;
    font-size: 108px;
    line-height: 162px;
    letter-spacing: -4px;
    color: var(--ink);
    list-style: none;
  }
  .headline .line { display: block; }
  .wedding .c1 { color: var(--navy); }
  .wedding .c2 { color: var(--sky); }
  .wedding .c3 { color: var(--orange); }
  .wedding .c4 { color: var(--gold); }
  .wedding .c5 { color: var(--flame); }
  .wedding .c6 { color: var(--red); }
  .wedding .c7 { color: var(--red); }
</style>
</head>
<body>
  <main class="invite">
    <div class="pattern-field" role="img" aria-label="Abstract woven pattern of orange, blue and yellow pixel bands"></div>
    <div class="light-column"></div>
    <h1 class="headline">
      <span class="line">we</span>
      <span class="line">invite</span>
      <span class="line">you</span>
      <span class="line">to</span>
      <span class="line">our</span>
      <span class="line wedding"><span class="c1">W</span><span class="c2">e</span><span class="c3">d</span><span class="c4">d</span><span class="c5">i</span><span class="c6">n</span><span class="c7">g</span></span>
    </h1>
  </main>
</body>
</html>
```